Industrial Professional Business Card Design (Vantrel Systems)

Would like professional looking business cards. Not too busy leaning towards minimal. Should have a slogan like:
"Industrial Automation and Control".

We are a tech company that programs industrial PLC computers. We also develop custom hardware solutions. Please use the logo for inspiration.

Target Market(s)

Mining, industrial, processing, automation, factory

Industry/Entity Type

Engineering

Contact Information for Business Card

Name, phone, email, website. job title.

Font styles to use
Other font styles liked:
• droid sans

Requirements
Must have
• Use colours that go well with the logo. Not too busy design.

```html
<!DOCTYPE html>
<html lang="en">
<head>
<meta charset="utf-8">
<title>Vantrel Systems – Business Card</title>
<link href="https://fonts.googleapis.com/css2?family=Open+Sans:wght@400;700&display=swap" rel="stylesheet">
<style>
  :root {
    --backdrop: #3b3b3d;
    --navy: #1a2a5a;
    --navy-deep: #161c4e;
    --ocean: #206a94;
    --silver: #c9cacd;
    --orange: #ef6a1f;
    --paper: #fbfbfd;
    --ink: #1c1c22;
  }
  * { margin: 0; padding: 0; box-sizing: border-box; }
  html, body {
    width: 1200px; height: 901px; overflow: hidden;
    background: var(--backdrop);
    font-family: "Open Sans", sans-serif;
  }
  .canvas {
    position: relative; width: 1200px; height: 901px;
    display: flex; align-items: center; justify-content: center; gap: 34px;
  }
  .card {
    position: relative; width: 550px; height: 314px; overflow: hidden;
    box-shadow: 0 14px 30px rgba(0,0,0,.45);
  }

  /* Front */
  .card-front {
    background: linear-gradient(200deg, var(--navy-deep) 0%, var(--navy) 35%, var(--ocean) 100%);
    display: flex; flex-direction: column; align-items: center; justify-content: center;
  }
  .front-mark {
    width: 64px; height: 64px; border-radius: 50%;
    background: var(--silver); margin-bottom: 18px;
  }
  .front-brand {
    font-weight: 400; font-size: 40px; letter-spacing: 1px; line-height: 1;
    color: var(--silver);
  }
  .front-slogan {
    margin-top: 12px;
    font-size: 12px; letter-spacing: 2px; text-transform: uppercase;
    color: var(--silver);
  }

  /* Back */
  .card-back { background: var(--paper); }
  .back-brand {
    position: absolute; left: 40px; top: 46px;
    font-weight: 400; font-size: 34px; letter-spacing: .5px; line-height: 1;
    color: var(--navy);
  }
  .back-slogan {
    position: absolute; left: 41px; top: 92px;
    font-size: 11px; letter-spacing: 1.5px; text-transform: uppercase;
    color: var(--orange);
  }
  .back-mark {
    position: absolute; right: 38px; top: 40px;
    width: 170px; height: 170px; border-radius: 50%;
    background: var(--orange);
  }
  .person { position: absolute; left: 40px; top: 172px; }
  .person-name { font-weight: 700; font-size: 20px; color: var(--navy); line-height: 1.15; }
  .person-title { font-weight: 400; font-size: 13px; color: var(--ink); }
  .contacts { position: absolute; left: 40px; top: 232px; list-style: none; }
  .contacts li {
    display: flex; align-items: center; gap: 10px;
    font-size: 12px; color: var(--ink); line-height: 20px;
  }
  .contacts svg { width: 13px; height: 13px; flex: none; }
</style>
</head>
<body>
<main class="canvas">
  <section class="card card-front" aria-label="Card front">
    <span class="front-mark"></span>
    <div class="front-brand">Vantrel Systems</div>
    <div class="front-slogan">Industrial Automation and Control</div>
  </section>

  <section class="card card-back" aria-label="Card back">
    <div class="back-brand">Vantrel Systems</div>
    <div class="back-slogan">Industrial Automation and Control</div>
    <span class="back-mark"></span>
    <div class="person">
      <div class="person-name">Marcus Hale</div>
      <div class="person-title">President</div>
    </div>
    <ul class="contacts">
      <li>
        <svg viewBox="0 0 16 16" aria-hidden="true"><path fill="#1a2a5a" d="M3.5 1.5l2.5 0 1 3.5-1.6 1.2a8 8 0 0 0 4.4 4.4L11 9l3.5 1v2.5c0 1-1 2-2 2A11 11 0 0 1 1.5 3.5c0-1 1-2 2-2z"/></svg>
        +44 555 014 2290
      </li>
      <li>
        <svg viewBox="0 0 16 16" aria-hidden="true"><rect x="1.5" y="3.5" width="13" height="9" fill="none" stroke="#1a2a5a" stroke-width="1.3"/><path d="M1.5 3.5L8 9l6.5-5.5" fill="none" stroke="#1a2a5a" stroke-width="1.3"/></svg>
        info@vantrelsystems.com
      </li>
      <li>
        <svg viewBox="0 0 16 16" aria-hidden="true"><g fill="none" stroke="#1a2a5a" stroke-width="1.2"><circle cx="8" cy="8" r="6.5"/><ellipse cx="8" cy="8" rx="3" ry="6.5"/><path d="M1.5 8h13M2.5 4.8h11M2.5 11.2h11"/></g></svg>
        www.vantrelsystems.com
      </li>
    </ul>
  </section>
</main>
</body>
</html>
```